The Lantern Guide

I am a life coach specializing in helping people with depression and bipolar disorder. I would like a nice, fun design for a business card.

```html
<!DOCTYPE html>
<html lang="en">
<head>
<meta charset="utf-8">
<title>The Lantern Guide – Business Card</title>
<link rel="stylesheet" href="https://fonts.googleapis.com/css2?family=Arimo:wght@700&family=Inter:wght@200&display=swap">
<style>
  :root {
    --paper: #ffffff;
    --mint-light: #b9fdc9;
    --mint-deep: #a7fdba;
    --mint-pale: #d5fede;
    --mint-text: #7ef59a;
    --ink-white: #ffffff;
  }
  html, body {
    margin: 0;
    padding: 0;
    overflow: hidden;
    background: var(--paper);
  }
  .card {
    position: relative;
    width: 1200px;
    height: 720px;
    overflow: hidden;
    background: var(--paper);
  }
  .card__shapes {
    position: absolute;
    inset: 0;
    display: block;
  }
  .shape--light { fill: var(--mint-light); }
  .shape--deep  { fill: var(--mint-deep); }
  .shape--pale  { fill: var(--mint-pale); }

  .brand {
    position: absolute;
    left: 0;
    right: 0;
    top: 92px;
    margin: 0;
    text-align: center;
    font-family: "Arimo", Arial, sans-serif;
    font-weight: 700;
    font-size: 140px;
    line-height: 138px;
    letter-spacing: -2px;
    color: var(--ink-white);
  }
  .brand__line { display: block; }

  .contact {
    position: absolute;
    top: 522px;
    margin: 0;
    font-family: "Inter", "Helvetica Neue", sans-serif;
    font-weight: 200;
    font-size: 50px;
    line-height: 62px;
    letter-spacing: -1px;
  }
  .contact__line { display: block; }
  .contact--person {
    left: 97px;
    text-align: left;
    color: var(--mint-text);
  }
  .contact--reach {
    right: 101px;
    text-align: right;
    color: var(--ink-white);
  }
</style>
</head>
<body>
  <main class="card">
    <svg class="card__shapes" width="1200" height="720" viewBox="0 0 1200 720" aria-hidden="true">
      <polygon class="shape--light" points="19,0 1200,0 1200,720 493,720"/>
      <polygon class="shape--deep" points="411.5,596.2 1200,208 1200,720 493,720"/>
      <polygon class="shape--pale" points="160,720 411.5,596.2 493,720"/>
    </svg>

    <h1 class="brand">
      <span class="brand__line">The Lantern</span>
      <span class="brand__line">Guide</span>
    </h1>

    <p class="contact contact--person">
      <span class="contact__line">Name</span>
      <span class="contact__line">Title</span>
    </p>

    <p class="contact contact--reach">
      <span class="contact__line">Phone #</span>
      <span class="contact__line">E-Mail</span>
    </p>
  </main>
</body>
</html>
```